Energy Healing for pregnant women postcard

I am an intuitive energy healer specializing in the care of pregnant women and their babies. I have an existing logo that is attached that should be placed on the card,sizing is at your discretion, recolor as needed. The message of the card should be one that conveys tranquility, growth, life and light. Images of pregnancy and motherhood could also fit well on the card, but that is not required if the preceding messages can be conveyed through other imagery. Also on the card, the following should appear: (company name and tag line)Positivity & JoyHealing the mind, body, spirit and soul with Energy provided to all living things by the Universe. Space should be left for my name and credentials on the front, while the address space on the back will be used for more contact information. Opposite the address block on the back, please leave room for a text box that will include benefits of the services. About 2"x3" should suffice.

Target Market(s)

Pregnant women and newly post-partum women

Industry/Entity Type

Health And Wellness

Font styles to use
Script

Colors
b05ba4
b768aa
d3a5cc
ecdaeb
e7f5f8
cfdeed
cee9f5
85cae6

Requirements
Must have
• Company logo. Company name. Tag line. Individual name and certifications
Nice to have
• Pictures or images that convey peace, tranquility healing and growth.
Should not have
• Anything harsh.

```html
<!DOCTYPE html>
<html lang="en">
<head>
<meta charset="utf-8">
<title>Harbor &amp; Wren – Energy Healing Postcard</title>
<link rel="stylesheet" href="https://fonts.googleapis.com/css2?family=Didact+Gothic&family=Lobster&display=swap">
<style>
  :root {
    --page: #eeeeec;
    --card: #ffffff;
    --aqua: #b3e0dd;
    --aqua-deep: #8ccfd6;
    --sky: #cfe9ef;
    --ink: #6a6a6a;
    --ink-soft: #7a7a7a;
    --sage: #8ea58b;
    --rule: #b9b9b9;
    --shadow: 0 6px 18px rgba(0,0,0,.28);
  }
  html, body {
    margin: 0;
    width: 856px;
    height: 1200px;
    overflow: hidden;
    background: var(--page);
  }
  .canvas { position: relative; width: 856px; height: 1200px; }

  .card {
    position: absolute;
    background: var(--card);
    box-shadow: var(--shadow);
    overflow: hidden;
    font-family: "Didact Gothic", sans-serif;
    color: var(--ink);
  }
  .card svg.shapes { position: absolute; inset: 0; }

  .brand-mark {
    position: absolute;
    font-family: "Lobster", cursive;
    color: var(--sage);
    text-align: center;
    white-space: nowrap;
  }
  .brand-mark span { display: block; }

  /* Front */
  .card--front { left: 64px; top: 65px; width: 662px; height: 513px; }
  .front-photo {
    position: absolute; inset: 0;
    background:
      radial-gradient(ellipse 160px 200px at 190px 250px, #e9ddd3 0%, rgba(233,221,211,0) 70%),
      radial-gradient(ellipse 260px 110px at 380px 330px, #f1ede8 0%, rgba(241,237,232,0) 75%),
      linear-gradient(180deg, #f5f6f6 0%, #ecefef 100%);
  }
  .credentials {
    position: absolute; right: 14px; top: 16px;
    text-align: right; font-size: 14.5px; line-height: 23px; color: var(--ink-soft);
  }
  .card--front .brand-mark {
    left: 452px; top: 180px; width: 160px;
    font-size: 32px; line-height: 42px;
  }
  .tagline {
    position: absolute; left: 0; right: 0; top: 430px; margin: 0;
    text-align: center; font-family: "Lobster", cursive;
    font-size: 23px; line-height: 32px; color: var(--ink);
  }

  /* Back */
  .card--back { left: 133px; top: 622px; width: 660px; height: 509px; }
  .back-photo {
    position: absolute; left: 0; top: 0; width: 360px; height: 214px;
    background:
      radial-gradient(ellipse 120px 140px at 210px 100px, #eec9b4 0%, rgba(238,201,180,0) 72%),
      radial-gradient(ellipse 90px 70px at 110px 150px, #f3d6c5 0%, rgba(243,214,197,0) 75%),
      linear-gradient(180deg, #f4f2f1 0%, #faf9f9 100%);
  }
  .back-name {
    position: absolute; left: 0; top: 214px; width: 378px; height: 72px;
    background: rgba(255,255,255,.92);
    text-align: center; font-size: 14.5px; line-height: 22px; padding-top: 12px; box-sizing: border-box;
  }
  .benefits {
    position: absolute; left: 20px; top: 302px; margin: 0; padding: 0;
    list-style: none; font-size: 15.5px; line-height: 26.6px; color: var(--ink);
  }
  .benefits li { display: flex; align-items: center; gap: 8px; }
  .benefits svg { flex: none; }
  .card--back .brand-mark {
    left: 392px; top: 34px; width: 130px;
    font-size: 24px; line-height: 32px;
  }
  .stamp-box {
    position: absolute; left: 549px; top: 25px; width: 92px; height: 73px;
    border: 2px solid #cfcfcf; box-sizing: border-box;
  }
  .address-line {
    position: absolute; left: 421px; width: 221px; height: 0;
    border-top: 1.5px solid var(--rule);
  }
</style>
</head>
<body>
<main class="canvas">

  <section class="card card--front">
    <div class="front-photo" role="img" aria-label="Photo of a mother in white holding her baby up to kiss its foot, soft bright room"></div>
    <svg class="shapes" viewBox="0 0 662 513" width="662" height="513" aria-hidden="true">
      <path d="M0 0 H662 V50 C560 42 470 80 360 84 C240 88 120 70 0 110 Z" fill="#ffffff" opacity=".85"/>
      <path d="M0 104 C110 70 230 86 350 82 C470 78 560 40 662 46 V58 C560 54 470 92 352 96 C230 100 120 92 0 122 Z" fill="var(--aqua-deep)" opacity=".75"/>
      <path d="M0 122 C120 94 230 104 352 98 C470 92 560 62 662 60 V70 C560 76 470 104 354 110 C230 116 120 112 0 136 Z" fill="var(--sky)" opacity=".8"/>
      <path d="M0 400 C150 370 300 380 430 384 C540 388 610 378 662 360 V513 H0 Z" fill="var(--sky)" opacity=".85"/>
      <path d="M0 412 C150 392 300 400 440 402 C550 404 620 396 662 384 V513 H0 Z" fill="var(--aqua)"/>
    </svg>
    <div class="credentials">
      <div>Miriam L. Hart, MSN, RCMT</div>
      <div>Reiki Master Teacher, Archangelic Light Master Teacher</div>
    </div>
    <div class="brand-mark"><span>Harbor &amp;</span><span>Wren</span></div>
    <p class="tagline">Harbor &amp; Wren Healing the mind, body, spirit and soul with<br>Energy provided to all living things by the Universe.</p>
  </section>

  <section class="card card--back">
    <div class="back-photo" role="img" aria-label="Photo of a baby's small hand resting on an adult's open palm"></div>
    <svg class="shapes" viewBox="0 0 660 509" width="660" height="509" aria-hidden="true">
      <path d="M0 287 H392 C386 360 374 440 352 509 H0 Z" fill="var(--aqua)"/>
      <path d="M282 0 H300 C380 80 412 180 404 287 C398 380 380 450 362 509 H344 C366 440 386 370 390 287 C396 180 364 80 282 0 Z" fill="var(--sky)"/>
      <path d="M300 0 H312 C392 84 424 184 416 290 C410 380 392 450 374 509 H362 C380 450 398 380 404 287 C412 180 380 80 300 0 Z" fill="var(--aqua-deep)" opacity=".55"/>
    </svg>
    <div class="back-name">
      <div>Miriam L. Hart, MSN, RCMT</div>
      <div>Reiki Master Teacher, Archangelic Light Master Teacher</div>
    </div>
    <ul class="benefits">
      <li><svg width="13" height="13" viewBox="0 0 13 13"><circle cx="6.5" cy="6.5" r="5.5" fill="none" stroke="#7a7a7a"/><path d="M4.6 4 L7.2 6.5 L4.6 9 M6.6 4 L9.2 6.5 L6.6 9" fill="none" stroke="#7a7a7a"/></svg>Deep relaxation</li>
      <li><svg width="13" height="13" viewBox="0 0 13 13"><circle cx="6.5" cy="6.5" r="5.5" fill="none" stroke="#7a7a7a"/><path d="M4.6 4 L7.2 6.5 L4.6 9 M6.6 4 L9.2 6.5 L6.6 9" fill="none" stroke="#7a7a7a"/></svg>Decrease anxiety</li>
      <li><svg width="13" height="13" viewBox="0 0 13 13"><circle cx="6.5" cy="6.5" r="5.5" fill="none" stroke="#7a7a7a"/><path d="M4.6 4 L7.2 6.5 L4.6 9 M6.6 4 L9.2 6.5 L6.6 9" fill="none" stroke="#7a7a7a"/></svg>Decrease stress</li>
      <li><svg width="13" height="13" viewBox="0 0 13 13"><circle cx="6.5" cy="6.5" r="5.5" fill="none" stroke="#7a7a7a"/><path d="M4.6 4 L7.2 6.5 L4.6 9 M6.6 4 L9.2 6.5 L6.6 9" fill="none" stroke="#7a7a7a"/></svg>Decrease discomforts</li>
      <li><svg width="13" height="13" viewBox="0 0 13 13"><circle cx="6.5" cy="6.5" r="5.5" fill="none" stroke="#7a7a7a"/><path d="M4.6 4 L7.2 6.5 L4.6 9 M6.6 4 L9.2 6.5 L6.6 9" fill="none" stroke="#7a7a7a"/></svg>Promote feelings of wellbeing</li>
      <li><svg width="13" height="13" viewBox="0 0 13 13"><circle cx="6.5" cy="6.5" r="5.5" fill="none" stroke="#7a7a7a"/><path d="M4.6 4 L7.2 6.5 L4.6 9 M6.6 4 L9.2 6.5 L6.6 9" fill="none" stroke="#7a7a7a"/></svg>Promote balance</li>
      <li><svg width="13" height="13" viewBox="0 0 13 13"><circle cx="6.5" cy="6.5" r="5.5" fill="none" stroke="#7a7a7a"/><path d="M4.6 4 L7.2 6.5 L4.6 9 M6.6 4 L9.2 6.5 L6.6 9" fill="none" stroke="#7a7a7a"/></svg>Relieve physical discomforts of pregnancy</li>
    </ul>
    <div class="brand-mark"><span>Harbor &amp;</span><span>Wren</span></div>
    <div class="stamp-box"></div>
    <div class="address-line" style="top:228px"></div>
    <div class="address-line" style="top:272px"></div>
    <div class="address-line" style="top:313px"></div>
    <div class="address-line" style="top:354px"></div>
  </section>

</main>
</body>
</html>
```